Real Estate Investing company needs a business card design

We need a business card design for new Real Estate Investment Company called "Maple Ridge Ventures, LLC." We buy homes for cash and close quickly in any situation. Our company provides an easy and fast option for home owners who are in tough situations who need to sell their home fast and don't want realtor fees or other listing hassles. We also renovate and resell our homes which helps provide housing for the community. We would like to see designs that use the colors blue and white to match our company logo or other colors that may match our company logo. The final design should communicate trust and easy process.
Industry/Entity Type
Business
Contact Information for Business Card
Front should have company name and company logo. back of card should have company logo and area to list services.
Look and feel

```html
<!DOCTYPE html>
<html lang="en">
<head>
<meta charset="utf-8">
<title>Maple Ridge Ventures, LLC – Business Card</title>
<link rel="stylesheet" href="https://fonts.googleapis.com/css2?family=Exo+2:wght@600&family=PT+Sans:ital,wght@0,400;1,400&display=swap">
<style>
  :root {
    --page-bg: #9a9a9a;
    --brand-blue: #0b5ca8;
    --card-white: #f1f1f3;
    --band-dark: #222222;
    --text-light: #f2f2f2;
    --text-muted: #d9e3ef;
    --divider: #6a6a6a;
  }
  * { margin: 0; padding: 0; box-sizing: border-box; }
  html, body {
    width: 1105px;
    height: 1200px;
    overflow: hidden;
    background: var(--page-bg);
  }
  .canvas {
    position: relative;
    width: 1105px;
    height: 1200px;
  }
  .card {
    position: absolute;
    left: 172px;
    width: 760px;
    height: 434px;
    overflow: hidden;
  }
  .card--front { top: 120px; background: var(--card-white); }
  .card--back { top: 640px; background: var(--brand-blue); }

  /* Front */
  .brand {
    position: absolute;
    left: 0; right: 0;
    top: 92px;
    display: flex;
    justify-content: center;
    align-items: center;
    gap: 14px;
    font-family: "Exo 2", sans-serif;
    font-weight: 600;
    font-size: 40px;
    color: var(--brand-blue);
    letter-spacing: 0.5px;
  }
  .brand__square {
    width: 22px;
    height: 22px;
    background: var(--brand-blue);
  }
  .front__rule {
    position: absolute;
    left: 0; right: 0;
    top: 236px;
    height: 7px;
    background: var(--brand-blue);
  }
  .front__band {
    position: absolute;
    left: 0; right: 0;
    top: 243px;
    bottom: 0;
    background: var(--band-dark);
  }
  .person {
    position: absolute;
    right: 417px;
    top: 278px;
    text-align: right;
    font-family: "PT Sans", sans-serif;
    color: var(--text-light);
    font-size: 20px;
    line-height: 30px;
  }
  .person__name {
    font-family: "Exo 2", sans-serif;
    font-weight: 600;
    font-size: 29px;
    line-height: 34px;
    color: #1f78d1;
  }
  .person__role {
    font-family: "Exo 2", sans-serif;
    font-weight: 600;
    font-size: 20px;
    line-height: 30px;
    color: #ffffff;
  }
  .front__divider {
    position: absolute;
    left: 374px;
    top: 280px;
    width: 1px;
    height: 116px;
    background: var(--divider);
  }
  .contacts {
    position: absolute;
    left: 408px;
    top: 274px;
    list-style: none;
    font-family: "PT Sans", sans-serif;
    font-size: 20px;
    color: var(--text-light);
  }
  .contacts li {
    display: flex;
    align-items: center;
    gap: 12px;
    height: 30px;
  }
  .contacts svg {
    width: 18px;
    height: 18px;
    fill: #1f78d1;
    flex: none;
  }

  /* Back */
  .back__brand {
    position: absolute;
    left: 0; right: 0;
    top: 110px;
    display: flex;
    justify-content: center;
    align-items: center;
    gap: 14px;
    font-family: "Exo 2", sans-serif;
    font-weight: 600;
    font-size: 38px;
    color: var(--text-muted);
  }
  .back__brand .brand__square { background: var(--text-muted); }
  .services {
    position: absolute;
    left: 60px; right: 60px;
    top: 210px;
    text-align: center;
    font-family: "PT Sans", sans-serif;
    font-style: italic;
    font-size: 18.5px;
    line-height: 24px;
    color: var(--text-muted);
  }
  .services p + p { margin-top: 9px; }
</style>
</head>
<body>
<main class="canvas">

  <section class="card card--front" aria-label="Business card front">
    <div class="brand"><span class="brand__square"></span>Maple Ridge Ventures, LLC</div>
    <div class="front__rule"></div>
    <div class="front__band"></div>

    <div class="person">
      <div class="person__name">Daniel Reyes</div>
      <div class="person__role">CEO/Founder</div>
      <div>2140 Birchwood Court</div>
      <div>Juneau, Alaska 99801</div>
    </div>

    <div class="front__divider"></div>

    <ul class="contacts">
      <li>
        <svg viewBox="0 0 24 24" aria-hidden="true"><path d="M6.6 10.8a15.5 15.5 0 0 0 6.6 6.6l2.2-2.2c.3-.3.7-.4 1-.2 1.1.4 2.3.6 3.6.6.6 0 1 .4 1 1V20c0 .6-.4 1-1 1A17 17 0 0 1 3 4c0-.6.4-1 1-1h3.5c.6 0 1 .4 1 1 0 1.3.2 2.5.6 3.6.1.3 0 .7-.2 1z"/></svg>
        555 210 3847
      </li>
      <li>
        <svg viewBox="0 0 24 24" aria-hidden="true"><path d="M6 3h12v5H6zM4 9h16c1.1 0 2 .9 2 2v6h-4v4H6v-4H2v-6c0-1.1.9-2 2-2zm4 7v3h8v-3z"/></svg>
        555 210 3848
      </li>
      <li>
        <svg viewBox="0 0 24 24" aria-hidden="true"><path d="M3 5h18c.6 0 1 .4 1 1v1l-10 6L2 7V6c0-.6.4-1 1-1zm-1 4.3 10 6 10-6V18c0 .6-.4 1-1 1H3c-.6 0-1-.4-1-1z"/></svg>
        info@mapleridgeventures.com
      </li>
      <li>
        <svg viewBox="0 0 24 24" aria-hidden="true"><path d="M12 2a10 10 0 1 0 0 20 10 10 0 0 0 0-20zm-1 17.9A8 8 0 0 1 4.2 10l4.8 4.8V16c0 1.1.9 2 2 2zm6.9-2.5A2 2 0 0 0 16 16h-1v-3c0-.6-.4-1-1-1H8v-2h2c.6 0 1-.4 1-1V7h2c1.1 0 2-.9 2-2v-.4a8 8 0 0 1 2.9 12.8z"/></svg>
        www.mapleridgeventures.com
      </li>
    </ul>
  </section>

  <section class="card card--back" aria-label="Business card back">
    <div class="back__brand"><span class="brand__square"></span>Maple Ridge Ventures, LLC</div>
    <div class="services">
      <p>We buy homes for cash &amp; close quickly in any situation.</p>
      <p>We provide an easy &amp; fast option for home owners who are<br>in tough situations who need to sell their home fast and don't want<br>realtor fees or other listing hassles.</p>
      <p>We also renovate &amp; resell homes which helps provide<br>housing for the community.</p>
    </div>
  </section>

</main>
</body>
</html>
```